business card deign

Logo needs the following on it.
1. attached logo
2. Tagline - "Cold drinks, loud music, long nights...we bring it all!"
3. Name- Delia Fenwick, Founder and CPO
4. Address - 418 E. Harlow Avenue, Ste 2204, Tampa, FL. 33719
5. Phone - 720.555.0187

```html
<!DOCTYPE html>
<html lang="en">
<head>
<meta charset="utf-8">
<title>Hopwell business card</title>
<link rel="stylesheet" href="https://fonts.googleapis.com/css2?family=Montserrat:wght@400;500;700&display=swap">
<style>
  :root {
    --page: #e9e6e1;
    --card-dark: #1b1b1b;
    --card-light: #ffffff;
    --ink: #111111;
    --ink-soft: #2a2a2a;
    --emboss: #0c0c0c;
    --tagline: #e8e8e8;
    --rule: #8a8a8a;
    --mark-dark: #262626;
  }
  * { box-sizing: border-box; margin: 0; padding: 0; }
  html, body {
    width: 1200px; height: 931px; overflow: hidden;
    background: var(--page);
    font-family: "Montserrat", sans-serif;
  }
  .stage { position: relative; width: 1200px; height: 931px; }
  .card {
    position: absolute;
    width: 620px; height: 354px;
    border-radius: 22px;
    box-shadow: 0 10px 28px rgba(0,0,0,.22);
    overflow: hidden;
  }
  .card--back { left: 60px; top: 80px; background: var(--card-dark); }
  .card--front { left: 520px; top: 497px; background: var(--card-light); }

  .brand {
    display: flex; align-items: center; gap: 12px;
    font-weight: 700; letter-spacing: .32em; text-transform: uppercase;
    white-space: nowrap;
  }
  .brand__dot { border-radius: 50%; flex: none; }

  .card--back .brand {
    position: absolute; left: 0; right: 0; top: 134px;
    justify-content: center; font-size: 40px; color: var(--emboss);
  }
  .card--back .brand__dot { width: 26px; height: 26px; background: var(--mark-dark); }
  .tagline {
    position: absolute; left: 0; right: 0; bottom: 56px;
    text-align: center; color: var(--tagline);
    font-size: 15px; font-weight: 400; letter-spacing: .01em;
  }

  .card--front .brand {
    position: absolute; left: 40px; top: 156px;
    font-size: 30px; color: var(--ink);
  }
  .card--front .brand__dot { width: 20px; height: 20px; background: var(--ink); }
  .divider {
    position: absolute; left: 318px; top: 52px;
    width: 1px; height: 250px; background: var(--rule);
  }
  .contact { position: absolute; left: 346px; top: 58px; right: 24px; color: var(--ink-soft); }
  .contact__name { font-size: 25px; font-weight: 700; color: var(--ink); }
  .contact__role { font-size: 14px; margin-top: 4px; margin-bottom: 20px; }
  .contact__list { list-style: none; font-size: 13.5px; }
  .contact__list li { display: flex; align-items: center; gap: 10px; margin-bottom: 9px; }
  .contact__list svg { width: 15px; height: 15px; flex: none; }
  .contact__address { font-size: 13.5px; line-height: 1.45; margin-top: 12px; }
</style>
</head>
<body>
<main class="stage">
  <section class="card card--back">
    <div class="brand"><span class="brand__dot"></span>Hopwell</div>
    <p class="tagline">Cold drinks, loud music, long nights...we bring it all!</p>
  </section>

  <section class="card card--front">
    <div class="brand"><span class="brand__dot"></span>Hopwell</div>
    <div class="divider"></div>
    <div class="contact">
      <h1 class="contact__name">Delia Fenwick</h1>
      <p class="contact__role">Founder and CPO</p>
      <ul class="contact__list">
        <li>
          <svg viewBox="0 0 24 24" aria-hidden="true"><path fill="#111" d="M6.6 10.8a15.1 15.1 0 0 0 6.6 6.6l2.2-2.2a1 1 0 0 1 1-.25 11.4 11.4 0 0 0 3.6.57 1 1 0 0 1 1 1V20a1 1 0 0 1-1 1A17 17 0 0 1 3 4a1 1 0 0 1 1-1h3.5a1 1 0 0 1 1 1c0 1.25.2 2.45.57 3.6a1 1 0 0 1-.25 1z"/></svg>
          720.555.0187
        </li>
        <li>
          <svg viewBox="0 0 24 24" aria-hidden="true"><path fill="#111" d="M2 5h20v14H2z"/><path fill="none" stroke="#fff" stroke-width="1.6" d="M2.5 5.5 12 13l9.5-7.5"/></svg>
          hello@hopwellco.com
        </li>
        <li>
          <svg viewBox="0 0 24 24" aria-hidden="true"><g fill="none" stroke="#111" stroke-width="2"><circle cx="12" cy="12" r="9"/><ellipse cx="12" cy="12" rx="4" ry="9"/><path d="M3 12h18M4.5 7.5h15M4.5 16.5h15"/></g></svg>
          www.hopwellco.com
        </li>
      </ul>
      <p class="contact__address">418 E. Harlow Avenue, Ste 2204,<br>Tampa, FL. 33719</p>
    </div>
  </section>
</main>
</body>
</html>
```